We are committed to helping players reach Football greatness!

Target Market(s)

Sports enthusiasts between 9 to 18 and their parents of all backgrounds.

Contact Information for Business Card

Harbor Football Academy
Marcus Delacourt
Head Coach
0452 318 627
harborfta@mailnest.test

Logo Text

Harbor Football Academy

Logo styles of interest
Abstract Logo
Requirements
Must have
• I want the logo to be representing football (soccer) and try and make it as 3D as possible please.
Nice to have
• As above mentioned make it represent a Football (soccer) theme please.
Should not have
• Nothing non-child friendly please.

```html
<!DOCTYPE html>
<html lang="en">
<head>
<meta charset="utf-8">
<title>Harbor Football Academy – Business Card</title>
<link href="https://fonts.googleapis.com/css2?family=Crimson+Pro:wght@500;700&display=swap" rel="stylesheet">
<style>
  :root {
    --backdrop: #e6e7e9;
    --card: #ffffff;
    --ink: #4a1a16;
    --brand: #8e1c2e;
    --accent-red: rgba(236, 120, 120, 0.55);
    --ball-tone: #e6d6c8;
    --wave-warm: #efd9b8;
    --wave-cool: #dfe6ec;
  }
  html, body {
    margin: 0;
    width: 1200px;
    height: 1000px;
    overflow: hidden;
    background: var(--backdrop);
  }
  .card {
    position: absolute;
    left: 194px;
    top: 266px;
    width: 812px;
    height: 467px;
    background: var(--card);
    overflow: hidden;
    font-family: "Crimson Pro", Georgia, serif;
    color: var(--ink);
  }
  .card__vignette {
    position: absolute;
    inset: 0;
    background: radial-gradient(ellipse 75% 80% at 50% 45%, rgba(255,255,255,0) 60%, var(--accent-red) 100%);
  }
  .card__ball-art {
    position: absolute;
    left: 450px;
    top: -30px;
    width: 490px;
    height: 490px;
    border-radius: 50%;
    background: radial-gradient(circle at 50% 45%, rgba(230,214,200,0.85) 0%, rgba(230,214,200,0.55) 55%, rgba(240,232,226,0.25) 100%);
  }
  .card__wave-art {
    position: absolute;
    left: 0;
    bottom: 0;
    width: 100%;
    height: 160px;
    background: linear-gradient(175deg, rgba(255,255,255,0) 10%, var(--wave-cool) 45%, var(--wave-warm) 65%, rgba(255,255,255,0.6) 100%);
    opacity: 0.8;
  }
  .brand {
    position: absolute;
    left: 40px;
    top: 118px;
    width: 420px;
    text-align: center;
  }
  .brand__mark {
    display: block;
    width: 70px;
    height: 70px;
    margin: 0 auto 14px;
    border-radius: 50%;
    background: var(--brand);
  }
  .brand__name {
    margin: 0;
    font-weight: 700;
    font-size: 36px;
    line-height: 1;
    color: var(--brand);
  }
  .divider {
    position: absolute;
    left: 495px;
    top: 128px;
    width: 2px;
    height: 142px;
    background: linear-gradient(to bottom, rgba(74,26,22,0), var(--ink) 30%, var(--ink) 70%, rgba(74,26,22,0));
  }
  .contact {
    position: absolute;
    left: 546px;
    top: 138px;
  }
  .contact__name {
    margin: 0;
    font-weight: 700;
    font-size: 24px;
    line-height: 1.1;
  }
  .contact__role {
    margin: 2px 0 0;
    font-weight: 500;
    font-size: 19px;
  }
  .contact__list {
    list-style: none;
    margin: 22px 0 0;
    padding: 0;
    font-weight: 700;
    font-size: 18px;
    line-height: 24px;
  }
  .contact__item {
    display: flex;
    align-items: center;
    gap: 8px;
  }
  .contact__icon { width: 18px; height: 18px; flex: none; }
</style>
</head>
<body>
  <div class="card">
    <div class="card__ball-art" role="img" aria-label="Large faint football decoration"></div>
    <div class="card__wave-art" role="img" aria-label="Soft flowing wave lines decoration"></div>
    <div class="card__vignette"></div>

    <div class="brand">
      <span class="brand__mark"></span>
      <p class="brand__name">Harbor Football Academy</p>
    </div>

    <div class="divider"></div>

    <div class="contact">
      <p class="contact__name">Marcus Delacourt</p>
      <p class="contact__role">Head Coach</p>
      <ul class="contact__list">
        <li class="contact__item">
          <svg class="contact__icon" viewBox="0 0 24 24" aria-hidden="true">
            <path fill="var(--ink)" d="M6.6 10.8a15.1 15.1 0 0 0 6.6 6.6l2.2-2.2a1 1 0 0 1 1-.25 11.4 11.4 0 0 0 3.6.57 1 1 0 0 1 1 1V20a1 1 0 0 1-1 1A17 17 0 0 1 3 4a1 1 0 0 1 1-1h3.5a1 1 0 0 1 1 1c0 1.25.2 2.45.57 3.57a1 1 0 0 1-.25 1z"/>
          </svg>
          <span>0452 318 627</span>
        </li>
        <li class="contact__item">
          <svg class="contact__icon" viewBox="0 0 24 24" aria-hidden="true">
            <rect x="2" y="5" width="20" height="14" rx="2" fill="var(--ink)"/>
            <path d="M3 6.5l9 6.5 9-6.5" fill="none" stroke="#fff" stroke-width="1.8"/>
          </svg>
          <span>harborfta@mailnest.test</span>
        </li>
      </ul>
    </div>
  </div>
</body>
</html>
```